Wholistic Health Clinic (Chiropractic Osteopathic Naturapathic Homeopathic New Website Design

Create a beautiful website for Fenwick Chiropractic clinic that has been in the Sutherland Shire for over 40 years, that exemplifies the passion for helping people with their health goals using that may include a variety of techniques including Chiropractic, Osteopathy, Acupuncture, Applied Kinesiology, Retained Neonatal Reflexes, Nutritional Advice, Exercise Prescription, Decompression therapy, Massage and Stress management techniques.
We have a wholistic approach that includes Nutritional, Emotional and Physical health

(A more detailed draft will be supplied shortly)

Pages:
Home page
About Us Page
Team Page
Contact page
Terms of service Page
Privacy Page
and any other relevant page(s)

Will supply photos for:
- The Team Page and their qualifications & brief resume
- About Us page

Will supply logos for:
BPN
TORVEX
PLORIVEN
GRANTLEAF
MVA
KPO

Target Market(s)

main target Parents of young children and those 20's to 60's who live in the Sutherland Shire & have disposable income (that said almost everybody would benefit from their services)

Coding

Coded - Design and coding required

Number of Pages Required

5+ page

Font styles to use
Sans Serif

Requirements
Must have
• Please follow the brief

1. Easy to manage ourselves to add alerts (like Covid 19 compliance & Harbel week etc.) & update content like photos of team members etc.
2. Must be responsive and look good on mobile devices
3. must be fast loading
4. Logo on every page
5. Easy navigation on every page
6. Phone number must be clickable
7. Terms of service & Privacy pages
8. Slider on page 1 using photo of healthy people of all ages enjoying various lifestyles & ability to add other photos easily
Should not have
• no testimonials or any non compliant elements according to the BPN

```html
<!DOCTYPE html>
<html lang="en">
<head>
<meta charset="utf-8">
<title>Fenwick Chiropractic – Wholistic Health Clinic</title>
<link href="https://fonts.googleapis.com/css2?family=Khand:wght@500;600&family=Lato:wght@400;700;900&display=swap" rel="stylesheet">
<style>
:root{
  --blue:#5b6db2;
  --blue-dark:#4a5a9a;
  --ink:#222;
  --text:#444;
  --muted:#eceef2;
  --dark:#2b2b2b;
  --footer:#262626;
  --white:#fff;
}
*{box-sizing:border-box;margin:0;padding:0}
html,body{width:1200px;height:3570px;overflow:hidden}
body{font-family:"Lato",sans-serif;color:var(--text);background:var(--white);position:relative}
.abs{position:absolute}
.display{font-family:"Khand",sans-serif;font-weight:600;color:var(--ink);text-transform:uppercase;letter-spacing:.3px}

/* Hero */
.hero{position:absolute;left:0;top:0;width:1200px;height:581px;background:linear-gradient(180deg,#2f5fb0 0%,#6f9bd8 40%,#c9d9ee 70%,#7fa262 88%,#4b7a32 100%)}
.brand{position:absolute;left:82px;top:30px;display:flex;align-items:center;gap:10px;color:var(--white)}
.brand-dot{width:34px;height:34px;border-radius:50%;background:var(--white);opacity:.9}
.brand-name{font-size:15px;line-height:1}
.brand-sub{font-size:8px;letter-spacing:.3px;margin-top:3px}
.nav{position:absolute;top:48px;left:611px;display:flex;gap:0;font-size:13px;font-weight:700;color:var(--white)}
.nav span{position:absolute;white-space:nowrap}
.phone{position:absolute;left:978px;top:46px;color:var(--white);font-size:13px;font-weight:700;display:flex;align-items:center;gap:6px}
.social-top{position:absolute;left:1040px;top:13px;display:flex;gap:10px}
.social-top i{width:20px;height:20px;border-radius:50%;display:block}
.header-rule{position:absolute;left:79px;top:86px;width:1041px;height:1px;background:rgba(255,255,255,.35)}
.hero-caption{position:absolute;left:79px;top:211px;width:374px;height:130px;background:rgba(255,255,255,.72);padding:16px 14px}
.hero-caption h1{font-family:"Khand",sans-serif;font-weight:500;font-size:29px;line-height:27px;color:#111}
.hero-caption p{font-size:12px;line-height:16px;color:#222;margin-top:8px}
.thumb{position:absolute;top:489px;width:143px;height:81px;border:3px solid var(--white)}
.arrow{position:absolute;top:512px}

/* Features */
.feature{position:absolute;top:672px;width:306px}
.feature .ph{height:186px}
.feature h2{font-size:23px;margin-top:30px}
.feature p{font-size:14px;line-height:18.5px;margin-top:12px;color:#444}
.more{display:block;margin-top:18px;font-size:12px;font-weight:700;color:var(--blue)}

/* About */
.about{position:absolute;left:0;top:1105px;width:1200px;height:722px;background:var(--muted)}
.about h2{position:absolute;left:76px;top:50px;font-size:38px}
.acc{position:absolute;left:82px;font-family:"Khand",sans-serif;font-weight:500;font-size:19px;color:var(--ink);text-transform:uppercase}
.acc b{font-weight:500;display:inline-block;width:18px}
.panel{position:absolute;left:79px;top:160px;width:1026px;height:280px;border:1px solid #9a9aa3}
.panel .diagram{position:absolute;left:48px;top:55px;width:184px;height:183px;background:linear-gradient(135deg,#fafafa,#e4dcd2)}
.panel .copy{position:absolute;left:272px;top:68px;width:700px;font-size:14px;line-height:18.5px;color:#444}
.panel .copy p+p{margin-top:19px}

/* Team */
.section-title{position:absolute;left:0;width:1200px;text-align:center;font-size:35px}
.divider{position:absolute;width:382px;height:14px}
.card{position:absolute;top:2033px;width:224px;height:319px;border:1px solid var(--blue);background:#f4f4f6;overflow:hidden}
.card .ph{height:243px;background:linear-gradient(180deg,#f2f2f2,#dfe3ea)}
.card .band{position:absolute;left:0;bottom:0;width:100%;height:76px;background:var(--blue);color:var(--white);text-align:center;padding-top:13px}
.card .name{font-size:14px;font-weight:900;line-height:16px}
.card .role{font-size:10.5px;margin-top:2px}
.card.open .ph{height:108px}
.card.open .band{height:211px;padding-top:19px}
.card .bio{font-size:10.5px;line-height:17px;padding:12px 14px 0}
.card .btn{display:inline-block;margin-top:14px;background:var(--white);color:var(--ink);font-size:12px;font-weight:700;padding:5px 12px}

/* Wellness */
.well{position:absolute;left:0;top:2449px;width:1200px;height:591px;background:linear-gradient(120deg,#4a4a4a,#2e2e2e 50%,#4b4540)}
.well .section-title{color:var(--white)}
.circle{position:absolute;top:2629px;width:194px;height:194px;border-radius:50%}
.pillar{position:absolute;top:2843px;width:280px;text-align:center;color:var(--white)}
.pillar h3{font-size:19px;font-weight:700;letter-spacing:.3px}
.pillar p{font-size:15px;line-height:20.5px;margin-top:9px}

/* Partners + alert */
.partner-name{position:absolute;left:172px;top:3094px;font-size:44px;font-weight:900;color:var(--blue);display:flex;align-items:center;gap:10px}
.partner-name i{width:22px;height:22px;border-radius:50%;background:var(--blue);display:block}
.partner-text{position:absolute;left:341px;top:3094px;width:700px;font-size:15px;line-height:21px;color:#444}
.alert{position:absolute;left:0;top:3198px;width:1200px;height:67px;background:var(--blue);color:var(--white);font-size:16px;text-align:center;line-height:67px}

/* Footer */
.footer{position:absolute;left:0;top:3265px;width:1200px;height:305px;background:var(--footer);color:#ddd}
.f-brand{position:absolute;left:128px;top:50px;width:160px;text-align:center;color:var(--white)}
.f-brand i{display:block;width:70px;height:70px;border-radius:50%;background:var(--white);margin:0 auto 14px}
.f-brand .n{font-size:15px}
.f-brand .s{font-size:9px;margin-top:2px}
.f-social{position:absolute;left:128px;top:212px;display:flex;gap:34px}
.f-social i{width:13px;height:13px;border-radius:50%;background:#ddd;display:block}
.f-col{position:absolute;top:54px;font-size:13px}
.f-col h4{font-size:20px;font-weight:700;color:var(--white);margin-bottom:22px}
.f-row{display:flex;gap:12px;margin-bottom:14px;line-height:17px}
.f-row svg{flex:none;margin-top:2px}
.f-links div{margin-bottom:12px;padding-left:6px}
.hours{font-size:11.5px;font-weight:700}
.f-rule{position:absolute;left:118px;top:253px;width:968px;height:1px;background:#444}
.copyright{position:absolute;left:134px;top:266px;font-size:13px}
.legal{position:absolute;left:870px;top:266px;font-size:13px}
</style>
</head>
<body>

<!-- Hero slider -->
<section class="hero" role="img" aria-label="Photo of a group of people jumping joyfully in a field under a blue sky">
</section>
<div class="brand">
  <span class="brand-dot"></span>
  <div><div class="brand-name">Fenwick Chiropractic</div><div class="brand-sub">WHOLISTIC HEALTH CLINIC</div></div>
</div>
<nav class="nav">
  <span style="left:0">HOME</span>
  <span style="left:74px">ABOUT US</span>
  <span style="left:172px">TEAM</span>
  <span style="left:243px">CONTACT US</span>
</nav>
<div class="phone">
  <svg width="16" height="16" viewBox="0 0 24 24"><path fill="#fff" d="M6.6 10.8a15 15 0 0 0 6.6 6.6l2.2-2.2c.3-.3.7-.4 1-.2 1.1.4 2.3.6 3.6.6.6 0 1 .4 1 1V20c0 .6-.4 1-1 1A17 17 0 0 1 3 4c0-.6.4-1 1-1h3.5c.6 0 1 .4 1 1 0 1.3.2 2.5.6 3.6.1.3 0 .7-.2 1z"/></svg>
  + (1800) 555 0142
</div>
<div class="social-top"><i style="background:#3b5998"></i><i style="background:#1da1f2"></i><i style="background:#d92b24"></i></div>
<div class="header-rule"></div>
<div class="hero-caption">
  <h1>Time to book in for a chiropractic or massage treatment today.</h1>
  <p>Sed ut perspiciatis undeom nis iste natus error sit volup tatem accusantium volup tatem</p>
</div>
<svg class="arrow" style="left:28px" width="20" height="30" viewBox="0 0 20 30"><path d="M15 4 5 15l10 11" stroke="#fff" stroke-width="4" fill="none"/></svg>
<svg class="arrow" style="left:1142px" width="20" height="30" viewBox="0 0 20 30"><path d="m5 4 10 11L5 26" stroke="#fff" stroke-width="4" fill="none"/></svg>
<div class="thumb" style="left:79px;background:linear-gradient(90deg,#f3f4f7,#a9c6df)" role="img" aria-label="Thumbnail: practitioner explaining a spine model"></div>
<div class="thumb" style="left:259px;background:linear-gradient(180deg,#3b6fc4,#8fb0de 70%,#4b7a32)" role="img" aria-label="Thumbnail: group jumping outdoors"></div>
<div class="thumb" style="left:438px;background:linear-gradient(180deg,#e5e5e5,#d7a9a0)" role="img" aria-label="Thumbnail: back with highlighted pain area"></div>
<div class="thumb" style="left:620px;background:linear-gradient(90deg,#dcdcdc,#f4f0ea)" role="img" aria-label="Thumbnail: senior patient with practitioner"></div>
<div class="thumb" style="left:798px;background:linear-gradient(90deg,#eeeeee,#d8c8b8)" role="img" aria-label="Thumbnail: massage treatment"></div>
<div class="thumb" style="left:977px;background:linear-gradient(90deg,#e8b9a8,#9fd6e8)" role="img" aria-label="Thumbnail: woman holding lower back at the beach"></div>

<!-- Intro features -->
<article class="feature" style="left:79px">
  <div class="ph" style="background:linear-gradient(90deg,#eef1f4,#b8d1e4)" role="img" aria-label="Photo of a practitioner showing a spine model to a patient"></div>
  <h2 class="display">Who we are</h2>
  <p>Fenwick Chiropractic, situated in Kellbrook and established for over 40 years, is passionate about helping you achieve your health care goals. &nbsp;We use a unique approach...</p>
  <a class="more">Find out More ›</a>
</article>
<article class="feature" style="left:448px">
  <div class="ph" style="background:linear-gradient(90deg,#d9d9d9,#a5a5a5)" role="img" aria-label="Photo of a practitioner examining a senior woman's neck"></div>
  <h2 class="display">What we do</h2>
  <p>We use many Chiropractic techniques in our clinic to help patients manage a range of musculoskeletal conditions and these are modified to all ages...</p>
  <a class="more">Find out More ›</a>
</article>
<article class="feature" style="left:808px">
  <div class="ph" style="background:linear-gradient(90deg,#9aa7b2,#d0d6db)" role="img" aria-label="Photo of a practitioner greeting an older patient"></div>
  <h2 class="display">What to expect</h2>
  <p>If you've never had Chiropractic before, don't worry. &nbsp;We will explain everything as we go and answer any of your questions as you have them.</p>
  <a class="more">Find out More ›</a>
</article>

<!-- About us accordion -->
<section class="about">
  <h2 class="display">About us</h2>
  <div class="acc" style="top:120px"><b>+</b>Chiropractic</div>
  <div class="panel">
    <div class="acc" style="left:3px;top:14px"><b>-</b>Applied Kinesiology</div>
    <div class="diagram" role="img" aria-label="Applied kinesiology triangle diagram with human figure and structure, chemical and mental labels"></div>
    <div class="copy">
      <p>A tool used only by health care practitioners registered to diagnose such as chiropractors, osteopaths, physiotherapists and medical practitioners.</p>
      <p>It is the use of manual muscle testing to evaluate the motor response of the nervous system to a sensory stimuli – a test of functional neurology.</p>
      <p>Applied Kinesiology provides immediate feedback to guide the best and most individualized care plan for you, removing interference to your nervous system and restoring normal function.</p>
    </div>
  </div>
  <div class="acc" style="top:465px"><b>+</b>Retained Neonatal Reflexes</div>
  <div class="acc" style="top:506px"><b>+</b>Chiropractic care during pregnancy</div>
  <div class="acc" style="top:548px"><b>+</b>Chiropractic for babies and children</div>
  <div class="acc" style="top:590px"><b>+</b>Sports Chiropractic</div>
  <div class="acc" style="top:630px"><b>+</b>Acupuncture and dry needling</div>
</section>

<!-- Team -->
<h2 class="section-title display" style="top:1905px">Meet our experts team</h2>
<svg class="divider" style="left:400px;top:1958px" viewBox="0 0 382 14"><line x1="0" y1="7" x2="180" y2="7" stroke="#888"/><line x1="202" y1="7" x2="382" y2="7" stroke="#888"/><circle cx="191" cy="7" r="4" fill="#444"/></svg>

<div class="card" style="left:161px">
  <div class="ph" role="img" aria-label="Portrait of a male chiropractor in a white coat"></div>
  <div class="band"><div class="name">DR OWEN PRESCOTT<br>DC., DO.</div><div class="role">(CHIROPRACTOR, OSTEOPATH)</div></div>
</div>
<div class="card open" style="left:482px">
  <div class="ph" role="img" aria-label="Portrait of a female chiropractor with glasses"></div>
  <div class="band">
    <div class="name">DR CLARA WENDELL<br>B.SC., M. CHIRO.</div>
    <div class="role">(CHIROPRACTOR)</div>
    <div class="bio">Clara Graduated from Ashdown University in 1999 with a Bachelor of Science and in 2001 with Masters of Chiropractic.</div>
    <span class="btn">Learn More</span>
  </div>
</div>
<div class="card" style="left:801px">
  <div class="ph" role="img" aria-label="Portrait of a female chiropractor holding a clipboard"></div>
  <div class="band"><div class="name">DR MAREN HOLLOWAY<br>B.SC. M. CHIRO.</div><div class="role">(CHIROPRACTOR)</div></div>
</div>

<!-- Wellness pillars -->
<section class="well" role="img" aria-label="Dimmed background photo of a practitioner treating a patient"></section>
<h2 class="section-title display" style="top:2503px;color:#fff">Subtext where best fits</h2>
<svg class="divider" style="left:405px;top:2557px" viewBox="0 0 382 14"><line x1="0" y1="7" x2="180" y2="7" stroke="#aaa"/><line x1="202" y1="7" x2="382" y2="7" stroke="#aaa"/><circle cx="191" cy="7" r="4" fill="#ddd"/></svg>
<div class="circle" style="left:125px;background:radial-gradient(circle,#5f9a3a,#c9533a 70%,#e8c8a0)" role="img" aria-label="Photo of a bowl of fresh salad"></div>
<div class="circle" style="left:496px;background:radial-gradient(circle at 50% 40%,#f2c6b0,#7ec8e8 75%)" role="img" aria-label="Photo of two fingertips with happy and sad drawn expressions"></div>
<div class="circle" style="left:841px;background:radial-gradient(circle,#8a3a3a,#b0b0b0 70%)" role="img" aria-label="Photo of a woman exercising in a gym"></div>
<div class="pillar" style="left:82px"><h3>NUTRITION</h3><p>At Fenwick Chiropractic we place great importance on the correct foods and nutritional supplements for optimal health &amp; wellbeing...</p></div>
<div class="pillar" style="left:453px"><h3>EMOTIONS</h3><p>The way you think affects the chemical and physical health of your body. We have various stress management techniques...</p></div>
<div class="pillar" style="left:798px"><h3>EXERCISE</h3><p>How you move your body greatly affects its function, either positively or negatively. &nbsp;We can help you rehabilitate following injury...</p></div>

<!-- Partners -->
<svg class="abs" style="left:84px;top:3108px" width="12" height="20" viewBox="0 0 12 20"><path d="M10 2 2 10l8 8" stroke="#333" stroke-width="2" fill="none"/></svg>
<div class="partner-name"><i></i>BPN</div>
<p class="partner-text">All our qualified practitioners are bound by the code of ethics of the Bayside Practitioners Network and meet continuing education requirements</p>
<svg class="abs" style="left:1097px;top:3108px" width="12" height="20" viewBox="0 0 12 20"><path d="m2 2 8 8-8 8" stroke="#333" stroke-width="2" fill="none"/></svg>

<div class="alert">ALERT: currently responding to <b>COVID-19</b>, spinal health week, promotions</div>

<!-- Footer -->
<footer class="footer">
  <div class="f-brand"><i></i><div class="n">Fenwick Chiropractic</div><div class="s">WHOLISTIC HEALTH CLINIC</div></div>
  <div class="f-social"><i></i><i></i><i></i><i></i></div>
  <div class="f-col" style="left:351px;width:240px">
    <h4>Contact Us</h4>
    <div class="f-row"><svg width="12" height="12" viewBox="0 0 24 24"><path fill="#ddd" d="M12 2a7 7 0 0 0-7 7c0 5 7 13 7 13s7-8 7-13a7 7 0 0 0-7-7zm0 9.5A2.5 2.5 0 1 1 12 6.5a2.5 2.5 0 0 1 0 5z"/></svg><span>Marrow Lane 4120 NB,<br>Eastvale Country</span></div>
    <div class="f-row"><svg width="12" height="12" viewBox="0 0 24 24"><path fill="#ddd" d="M6.6 10.8a15 15 0 0 0 6.6 6.6l2.2-2.2c.3-.3.7-.4 1-.2 1.1.4 2.3.6 3.6.6.6 0 1 .4 1 1V20c0 .6-.4 1-1 1A17 17 0 0 1 3 4c0-.6.4-1 1-1h3.5c.6 0 1 .4 1 1 0 1.3.2 2.5.6 3.6.1.3 0 .7-.2 1z"/></svg><span>02 5550 1742 , 0400 555 318</span></div>
    <div class="f-row"><svg width="12" height="12" viewBox="0 0 24 24"><rect x="2" y="5" width="20" height="14" rx="2" fill="none" stroke="#ddd" stroke-width="2"/><line x1="2" y1="10" x2="22" y2="10" stroke="#ddd" stroke-width="2"/></svg><span>www.fenwickchiro.example</span></div>
    <div class="f-row"><svg width="12" height="12" viewBox="0 0 24 24"><path fill="#ddd" d="M2 5h20v14H2zm2 2v.5l8 5 8-5V7z"/></svg><span>support@fenwickchiro.example</span></div>
  </div>
  <div class="f-col f-links" style="left:638px">
    <h4>Quick Links</h4>
    <div>HOME</div><div>ABOUT US</div><div>TEAM</div><div>CONTACT</div>
  </div>
  <div class="f-col hours" style="left:877px;width:240px">
    <h4>Clinic Hours</h4>
    <div class="f-row" style="margin-bottom:10px"><svg width="12" height="12" viewBox="0 0 24 24"><circle cx="12" cy="12" r="9" fill="none" stroke="#ddd" stroke-width="2"/><path d="M12 7v5l3 2" stroke="#ddd" stroke-width="2" fill="none"/></svg><span>MONDAY TO FRIDAY: 2PM - 6.45PM</span></div>
    <div class="f-row"><svg width="12" height="12" viewBox="0 0 24 24"><circle cx="12" cy="12" r="9" fill="none" stroke="#ddd" stroke-width="2"/><path d="M12 7v5l3 2" stroke="#ddd" stroke-width="2" fill="none"/></svg><span>SAT: 8AM – 12 NOON</span></div>
    <div style="margin:12px 0 8px;line-height:17px">CLINIC HOURS MAY VARY,<br>PLEASE CALL US.</div>
    <div class="f-row"><svg width="14" height="14" viewBox="0 0 24 24"><circle cx="12" cy="12" r="10" fill="none" stroke="#ddd" stroke-width="2"/><path fill="#ddd" d="M9 8.5a7 7 0 0 0 6.5 6.5l1-1.2-2-1-1 .8a5 5 0 0 1-2.2-2.2l.8-1-1-2z"/></svg><span>02 5550 1742 , 0400 555 318</span></div>
  </div>
  <div class="f-rule"></div>
  <div class="copyright">Copyright © 2020. Fenwick Chiropractic. All rights reserved</div>
  <div class="legal">Terms of service &nbsp;&nbsp;&nbsp; | &nbsp;&nbsp;&nbsp; Privacy</div>
</footer>

</body>
</html>
```